Real Estate Agent Service Brochure

I need a trifold brochure to showcase my real estate services. I am a veteran Real Estate Broker specializing in marketing properties for sale and for top dollar. I would like to see designs that use colors from my logo (attached) and I would like to showcase some before and after photos of staging jobs I have done to homes to get them ready for the market. This brochure is specific to home sellers. You are happy to go check out my website for inspiration www.lomavertpa.com but keep the copy as I have written it. The the final design should communicate experienced professional who uses current technologies and strategies to market properties for the highest value.

Target Market(s)

Homeowners wanting to sell their homes

Industry/Entity Type

Real Estate Agent

Font styles to use
Serif

Requirements
Must have
• My, logo, personal photo, title and contact information as listed:
• Marta Venholt
• Owner Broker
• Stager Re-Designer
• 860-912-7048
• BRAVE Realty LLC
• LOMAVERTPA.com
• Marta@LOMAVERTPA.com
• The colors used should be those in my logo.
• Brochure should be able to fit in standard envelope for mailing.
Nice to have
• I think I would like my personal photo and contact information on the front panel.
Should not have
• Bright colors.

```html
<!DOCTYPE html>
<html lang="en">
<head>
<meta charset="utf-8">
<title>BRAVE Realty LLC – Seller Brochure</title>
<link rel="stylesheet" href="https://fonts.googleapis.com/css2?family=Open+Sans:wght@400;600;700;800&display=swap">
<style>
  :root{
    --navy:#1d2357;
    --navy-deep:#151a45;
    --white:#ffffff;
    --ink:#2a2d3a;
    --mist:#e9eaee;
    --mist-dark:#cfd1d8;
    --wood-floor:#3b2c24;
  }
  *{box-sizing:border-box;margin:0;padding:0}
  html,body{width:895px;height:1200px;overflow:hidden}
  body{background:#f1f1f3;font-family:"Open Sans",Arial,sans-serif;color:var(--ink);position:relative}

  .spread{position:absolute;left:57px;width:780px;height:540px;background:var(--white);overflow:hidden;box-shadow:0 4px 14px rgba(0,0,0,.18)}
  .spread-outer{top:40px}
  .spread-inner{top:620px}
  .panel{position:absolute;top:0;width:260px;height:540px;overflow:hidden}
  .panel-1{left:0}.panel-2{left:260px}.panel-3{left:520px}
  .shapes{position:absolute;inset:0;width:260px;height:540px}

  .photo{position:absolute}
  .photo-kitchen-before{background:linear-gradient(160deg,#f2ede6 0%,#bdb3a6 45%,var(--wood-floor) 100%)}
  .photo-kitchen-after{background:linear-gradient(170deg,#f6f3ee 0%,#d6d1ca 50%,#4a3a30 100%)}
  .photo-living-fade{background:linear-gradient(180deg,rgba(255,255,255,0) 0%,#eeeeef 55%,#e2e1e0 100%)}
  .photo-portrait{background:linear-gradient(160deg,#6b5446 0%,#3c2d25 60%,#221a16 100%);border:4px solid var(--navy)}
  .photo-bedroom{background:linear-gradient(165deg,#f3f1ee 0%,#c9c2b8 55%,#5a4a3e 100%)}
  .photo-dining-before{background:linear-gradient(165deg,#efe9df 0%,#b7a88f 50%,#3d2e25 100%)}
  .photo-dining-after{background:linear-gradient(165deg,#f5f1ea 0%,#cdbfa8 50%,#6b4a30 100%)}

  .tag{position:absolute;font-weight:800;font-size:15px;letter-spacing:.5px;text-transform:uppercase}
  .tag-light{color:var(--white)}
  .tag-dark{color:var(--navy)}

  .body-copy{font-size:9.6px;line-height:1.38;text-align:justify}
  .body-copy p+p{margin-top:10px}

  .brand{position:absolute;display:flex;align-items:center;gap:6px;font-weight:800;color:var(--navy);letter-spacing:1px;white-space:nowrap}
  .brand-mark{width:10px;height:10px;background:var(--navy)}
  .brand-plate{position:absolute;left:70px;top:392px;width:120px;height:70px;background:var(--white);display:flex;align-items:center;justify-content:center}
  .brand-plate .brand{position:static;font-size:20px}

  .site-url{position:absolute;color:var(--white);font-weight:700;font-size:17px}

  .agent{position:absolute;right:18px;text-align:right;color:var(--navy)}
  .agent-name{font-size:16px;font-weight:800;text-transform:uppercase;line-height:1.1}
  .agent-title{font-size:12px;font-weight:700;text-transform:uppercase;line-height:1.15}
  .agent-subtitle{font-size:12px;font-weight:400;color:#6b6f80;line-height:1.15}
  .motto{position:absolute;right:40px;top:318px;text-align:right;color:var(--navy);font-weight:800;font-size:30px;line-height:.95;text-transform:uppercase}
  .contact{position:absolute;right:18px;top:432px;text-align:right;color:var(--ink);font-size:11px;line-height:1.3}

  .testimonials{position:absolute;left:20px;top:18px;width:222px}
  .testimonials h2{font-size:11.5px;font-weight:800;color:var(--navy);text-transform:uppercase;line-height:1.15;margin-bottom:6px}
  .testimonials p{font-size:8.8px;line-height:1.33;text-align:justify}
  .testimonials .signer{font-weight:700;color:var(--navy);margin-bottom:5px}

  .navy-copy{position:absolute;left:18px;top:16px;width:224px;color:var(--white);font-size:8.8px;line-height:1.36;text-align:justify}
  .navy-copy p+p{margin-top:8px}

  .knowledge{position:absolute;left:18px;top:400px;width:224px}
  .knowledge h2{font-size:11.5px;font-weight:800;color:var(--navy);text-transform:uppercase;margin-bottom:6px}
  .knowledge p{font-size:9.6px;line-height:1.36;text-align:justify}
</style>
</head>
<body>

<section class="spread spread-outer">

  <div class="panel panel-1">
    <div class="photo photo-kitchen-before" style="left:0;top:0;width:260px;height:292px" role="img" aria-label="Kitchen before staging, dark floors and bare island"></div>
    <div class="photo photo-kitchen-after" style="left:0;top:328px;width:260px;height:212px" role="img" aria-label="Kitchen and dining area after staging, set table with chandelier"></div>
    <svg class="shapes" viewBox="0 0 260 540" aria-hidden="true">
      <polygon points="0,292 260,268 260,300 0,328" fill="var(--white)"/>
      <polygon points="0,290 260,264 260,272 0,298" fill="var(--navy)"/>
    </svg>
    <span class="tag tag-light" style="left:150px;top:245px">Before</span>
    <span class="tag tag-dark" style="left:18px;top:300px">After</span>
  </div>

  <div class="panel panel-2">
    <div class="photo photo-living-fade" style="left:0;top:220px;width:260px;height:200px" role="img" aria-label="Softly faded staged living room with white sofa"></div>
    <div class="body-copy" style="position:absolute;left:20px;top:24px;width:220px">
      <p>Selling Real Estate has changed drastically in the last few years. Today's real estate processes are multi-faceted undertakings that encompass significant emotional and financial components. Having the right marketing partner is so important; one who works to protect your best interests while capably navigating you through the many complexities of the real estate transaction is vital.</p>
      <p>Marta Venholt Real Estate Marketing Specialist truly understands not only the legal process needed but also recognizes buyer trends and knows how to "showcase" a property to sell targeted to the proper consumer demographic.</p>
      <p>A home is one of your most valuable assets. If you are thinking about selling a property, it is crucial that you hire someone with an extraordinary history of happy sellers.</p>
    </div>
    <svg class="shapes" viewBox="0 0 260 540" aria-hidden="true">
      <polygon points="0,410 260,382 260,540 0,540" fill="var(--navy)"/>
    </svg>
    <div class="brand-plate"><div class="brand">BRAVE</div></div>
    <div class="site-url" style="left:56px;top:478px">LOMAVERTPA.com</div>
  </div>

  <div class="panel panel-3">
    <svg class="shapes" viewBox="0 0 260 540" aria-hidden="true">
      <rect x="0" y="225" width="260" height="240" fill="var(--mist)" opacity=".5"/>
      <rect x="0" y="50" width="260" height="3" fill="var(--navy)"/>
      <polygon points="150,540 260,470 260,540" fill="var(--navy)"/>
      <polygon points="0,540 0,520 150,540" fill="var(--navy)"/>
    </svg>
    <div class="brand" style="right:18px;top:14px;font-size:22px">BRAVE <span class="brand-mark"></span></div>
    <div class="photo photo-portrait" style="left:12px;top:62px;width:236px;height:168px" role="img" aria-label="Portrait of the broker in a dark blazer"></div>
    <div class="agent" style="top:238px">
      <div class="agent-name">Marta Venholt</div>
      <div class="agent-title">Owner Broker</div>
      <div class="agent-subtitle">Stager Re-Designer</div>
    </div>
    <div class="motto">Buy<br>Sell<br>Build</div>
    <div class="contact">860-912-7048<br>Marta@LOMAVERTPA.com<br>LOMAVERTPA.com</div>
  </div>
</section>

<section class="spread spread-inner">

  <div class="panel panel-1">
    <svg class="shapes" viewBox="0 0 260 540" aria-hidden="true">
      <rect x="0" y="400" width="260" height="140" fill="var(--mist)" opacity=".6"/>
      <path d="M0,425 Q130,470 260,520 L260,540 L0,540 Z" fill="var(--navy)"/>
      <path d="M0,410 Q130,455 260,505" fill="none" stroke="var(--mist-dark)" stroke-width="6"/>
    </svg>
    <div class="testimonials">
      <h2>This is what Marta's clients<br>say about their experiences:</h2>
      <p>In the Real Estate Business there are many, but none like Marta. She brings a level of professionalism far above any other Broker. She will have no trouble selling your house. What is different is her honesty, sincerity and unquestionable ethics. She will make sure that you are satisfied with every aspect of your transaction.</p>
      <p class="signer">Harold P.</p>
      <p>Marta and the team at Brave are knowledgeable and professional. I have been involved in three separate real estate transactions with Marta as my broker. I am always pleased and impressed by her negotiating skills, her market knowledge and her ability to manage the process.</p>
      <p class="signer">Lorna B.</p>
      <p>The marketing and staging of our house was on point. I don't think the sale of our home would have been as successful without it.</p>
      <p class="signer">Rob &amp; Celia T.</p>
      <p>Am so glad that we found Marta to help us in staging a property that we had just finished renovating. She listened to our ideas of what we envisioned in the spaces based on the style of the house and put it all together on time for the first open house that got rave reviews. Her combined background in real estate and interior design made her a perfect partner for our job.</p>
      <p class="signer">Wendy S.</p>
    </div>
  </div>

  <div class="panel panel-2">
    <svg class="shapes" viewBox="0 0 260 540" aria-hidden="true">
      <polygon points="0,0 260,0 260,275 0,235" fill="var(--navy)"/>
    </svg>
    <div class="navy-copy">
      <p>Marta devotes her efforts to selling real estate, by keeping up with the evolving market, researching buyer trends and preparing homes before they enter the market by staging them to connect with the target buyer. Marta knows all sales are not alike. Therefore, taking a cookie cutter approach is not acceptable; she recognizes that each property is unique and requires a personalized marketing plan and strategy.</p>
      <p>A veteran in the real estate industry with nearly 30 years expertise and consistent membership in the Multi-Million-Dollar Club combined with her HSC Home Stager and Re-Designer credentials assures that her clients get the advantage of vast knowledge, seasoned experience and proven results, all geared to creating beautiful spaces, which form a connection with the right buyer producing the highest and best offer.</p>
    </div>
    <div class="photo photo-bedroom" style="left:0;top:238px;width:260px;height:302px;clip-path:polygon(0 0,100% 13%,100% 100%,0 100%)" role="img" aria-label="Bedroom shown before and after staging"></div>
    <svg class="shapes" viewBox="0 0 260 540" aria-hidden="true">
      <polygon points="60,540 260,395 260,405 75,540" fill="var(--navy)"/>
    </svg>
    <span class="tag tag-light" style="left:22px;top:432px">Before</span>
    <span class="tag tag-light" style="left:168px;top:456px">After</span>
  </div>

  <div class="panel panel-3">
    <div class="photo photo-dining-before" style="left:0;top:0;width:260px;height:150px" role="img" aria-label="Kitchen and dining area before staging"></div>
    <div class="photo photo-dining-after" style="left:0;top:178px;width:260px;height:200px" role="img" aria-label="Kitchen and dining area after staging with set table and flowers"></div>
    <svg class="shapes" viewBox="0 0 260 540" aria-hidden="true">
      <polygon points="0,150 260,118 260,178 0,185" fill="var(--white)"/>
      <polygon points="0,146 260,114 260,121 0,153" fill="var(--navy)"/>
      <polygon points="0,378 260,352 260,540 0,540" fill="var(--white)"/>
      <polygon points="0,376 260,350 260,356 0,382" fill="var(--navy)"/>
      <rect x="0" y="470" width="260" height="70" fill="var(--mist)" opacity=".55"/>
    </svg>
    <span class="tag tag-light" style="left:160px;top:95px">Before</span>
    <span class="tag tag-dark" style="left:20px;top:150px">After</span>
    <div class="knowledge">
      <h2>Proven Market Knowledge</h2>
      <p>That's what you can expect when you work with seasoned specialist Marta Venholt for all your Real Estate needs. The sale of a home is too important an undertaking to entrust to just anyone. Select a dedicated, service-oriented and results-driven broker who understands the intricacies of the Real Estate process...select Marta.</p>
    </div>
  </div>
</section>

</body>
</html>
```